Business Card and Letterhead Design Project

I am starting my own building design business in Melbourne. The business will use my experience to help people make balanced life choices for building and renovating. My target audience is women -particularly mothers. I aim to be approachable and economical. I would like to see a design that uses greens or blues - natural colours. A lot of my work balances design and construction management so design should be flexible.

I want a double sided business card design and a letterhead design that I can use on all office correspondance

Design should have a clean crisp feel - a bit edgey in a feminine way.

Target Market(s)

Potential clients.

Industry/Entity Type

Construction

Requirements
Must have
• Harbourline Design Studio
Rosalind Tebbutt B.Arch

0498 273 461
rosalind@harbourlinedesignstudio.com.au

14 Quandong Street
Marlow Heath VIC 3191
harbourlinedesignstudio.com.au
Nice to have
• Should have a calming feel to make me seem approachable but still professional.
Should not have
• No photos on the card or building plans.

```html
<!DOCTYPE html>
<html lang="en">
<head>
<meta charset="utf-8">
<title>Harbourline Design Studio – Stationery</title>
<link rel="stylesheet" href="https://fonts.googleapis.com/css2?family=Archivo+Narrow:wght@600;700&family=Roboto+Slab:wght@300&display=swap">
<style>
  :root {
    --backdrop: #222222;
    --paper: #ffffff;
    --sky: #29aae1;
    --sky-edge: #1f74bd;
    --ocean-top: #22a8e0;
    --ocean-bottom: #0377cf;
    --navy: #0a3a9f;
    --mist: #f2f2f4;
    --mist-edge: #cdcdd0;
    --brand-blue: #1b98d6;
    --ink-light: #ffffff;
  }
  * { box-sizing: border-box; margin: 0; padding: 0; }
  html, body {
    width: 1200px; height: 1000px; overflow: hidden;
    background: var(--backdrop);
  }
  .canvas { position: relative; width: 1200px; height: 1000px; }

  /* Letterhead */
  .letterhead {
    position: absolute; left: 88px; top: 44px;
    width: 690px; height: 896px;
    background: var(--paper); overflow: hidden;
  }
  .letterhead svg.shapes { position: absolute; inset: 0; }
  .letterhead__title {
    position: absolute; left: 36px; top: 27px;
    font-family: "Archivo Narrow", sans-serif; font-weight: 600;
    font-size: 23px; color: var(--ink-light); letter-spacing: 0.1px;
  }
  .letterhead__footer {
    position: absolute; top: 836px; left: 14px; right: 11px;
    display: flex; justify-content: space-between; align-items: flex-start;
    font-family: "Archivo Narrow", sans-serif; font-weight: 700;
    font-size: 9px; line-height: 12.5px; color: var(--ink-light);
  }
  .letterhead__footer strong { font-size: 10px; }
  .letterhead__footer .studio { text-align: right; }

  /* Business cards */
  .card {
    position: absolute; overflow: hidden;
    box-shadow: 0 3px 8px rgba(0,0,0,0.45);
  }
  .card svg.shapes { position: absolute; inset: 0; }
  .card--front {
    left: 640px; top: 227px; width: 440px; height: 264px;
    background: var(--paper);
  }
  .card--front .brand {
    position: absolute; top: 128px; left: 0; right: 0; text-align: center;
    font-family: "Roboto Slab", serif; font-weight: 300;
    font-size: 18px; color: var(--brand-blue);
  }
  .card--back {
    left: 640px; top: 553px; width: 437px; height: 262px;
    background: var(--mist);
  }
  .card--back .details {
    position: absolute; left: 36px; top: 101px;
    font-family: "Roboto Slab", serif; font-weight: 300;
    color: var(--ink-light); font-size: 12.5px; line-height: 15.5px;
  }
  .card--back .details .brand { font-size: 14px; margin-bottom: 14px; }
  .card--back .details .address { margin-top: 9px; }
  .card--back .web {
    position: absolute; left: 0; right: 0; top: 237px; text-align: center;
    font-family: "Roboto Slab", serif; font-weight: 300;
    color: var(--ink-light); font-size: 12.5px;
  }
</style>
</head>
<body>
<div class="canvas">

  <section class="letterhead">
    <svg class="shapes" width="690" height="896" viewBox="0 0 690 896">
      <path fill="var(--sky-edge)" d="M0,0 H470 C440,50 360,88 240,98 C150,105 70,104 0,100 Z"/>
      <path fill="var(--sky)" d="M0,0 H460 C430,44 352,80 236,90 C148,97 70,96 0,92 Z"/>
      <path fill="var(--sky-edge)" d="M0,822 C140,808 300,800 460,804 C560,806 640,798 690,786 V896 H0 Z"/>
      <path fill="var(--sky)" d="M0,830 C140,816 300,810 460,813 C560,815 640,808 690,796 V896 H0 Z"/>
    </svg>
    <h1 class="letterhead__title">Harbourline Design Studio</h1>
    <div class="letterhead__footer">
      <div class="person">
        <strong>Rosalind Tebbutt B.Arch</strong><br>
        0498 273 461<br>
        rosalind@harbourlinedesignstudio.com.au
      </div>
      <div class="studio">
        <strong>Harbourline Design Studio</strong><br>
        14 Quandong Street<br>
        Marlow Heath VIC 3191<br>
        harbourlinedesignstudio.com.au
      </div>
    </div>
  </section>

  <section class="card card--front">
    <svg class="shapes" width="440" height="264" viewBox="0 0 440 264">
      <defs>
        <linearGradient id="frontSea" x1="0" y1="0" x2="0" y2="1">
          <stop offset="0" stop-color="#0a8ddc"/>
          <stop offset="1" stop-color="var(--ocean-bottom)"/>
        </linearGradient>
      </defs>
      <path fill="var(--navy)" d="M0,212 C120,204 260,196 440,176 V264 H0 Z"/>
      <path fill="url(#frontSea)" d="M0,218 C120,212 270,204 440,186 V264 H0 Z"/>
    </svg>
    <p class="brand">Harbourline Design Studio</p>
  </section>

  <section class="card card--back">
    <svg class="shapes" width="437" height="262" viewBox="0 0 437 262">
      <defs>
        <linearGradient id="backSea" x1="0" y1="0" x2="0" y2="1">
          <stop offset="0" stop-color="var(--ocean-top)"/>
          <stop offset="0.45" stop-color="#15a0dd"/>
          <stop offset="1" stop-color="var(--ocean-bottom)"/>
        </linearGradient>
      </defs>
      <path fill="var(--mist-edge)" d="M0,58 C130,50 280,38 437,22 V262 H0 Z"/>
      <path fill="url(#backSea)" d="M0,64 C130,58 280,48 437,34 V262 H0 Z"/>
    </svg>
    <div class="details">
      <p class="brand">Harbourline Design Studio</p>
      <p>Rosalind Tebbutt B.Arch<br>0498 273 461<br>rosalind@harbourlinedesignstudio.com.au</p>
      <p class="address">14 Quandong Street, Marlow Heath VIC 3191</p>
    </div>
    <p class="web">harbourlinedesignstudio.com.au</p>
  </section>

</div>
</body>
</html>
```